International Flower distributer needs a landing page

We are looking to have a landing page made that will be easy to maintain and upload more content as our business grows.

We like the template designs and ease of use of Pagelofty. We'd explore other host sites.

Hello,

To start we would like something that can be managed and updated on a platform like pagelofty. We like page lofty because of the premade designs and flexibility.

Website requirements:

- About us:

- Verdant Hollow Corp - Established 1999

- Marla Pruett - Founder

- Danielle Pruett - Account Executive

- Gerald Pruett - Director of Operations

- Rosalba Penwick - (Jill's Job Description?)

- Natalia Ferreira (Make us look like a bigger company with more staff)

What we do:

- Personalized Customer service

- Exclusively Mass market experience to meet high demands

- Dedicated team assigned to your account

How we do it:

- Partnerships with farms in COlombia, ecuador and costa rica

- Farm fresh delivered directly from cargo planes to state of the art cooler facility at Delmont Airport

- Canopy trust?

Products we Sell:

- Farm made bouquets

- Consumer Bunches

- Programs Tailored to fit customer's retail program

For more Information:

- Gerald and Danielle phone and email

- Submit email inquiry

Corporate buyers that want to verify who we are and get our contact information

Floral, but not a flower shop. We import farm fresh cut flowers from south america and send them directly to supermarkets around the country.

• We are not selling anything on the website. We sell business to business.

```html
<!DOCTYPE html>
<html lang="en">
<head>
<meta charset="utf-8">
<title>Verdant Hollow Corp</title>
<link rel="stylesheet" href="https://fonts.googleapis.com/css2?family=Gilda+Display&family=Roboto:wght@400;500;700&display=swap">
<style>
:root{
  --paper:#f4f3ee;
  --navy:#2e3192;
  --green:#8cc63f;
  --ink:#33334a;
  --muted:#6b6b78;
  --orange:#f7931e;
  --band:#e8edda;
  --white:#ffffff;
  --line:#e2e2e2;
}
*{box-sizing:border-box;margin:0;padding:0}
html,body{width:1200px;height:3125px;overflow:hidden}
body{background:var(--paper);font-family:"Roboto",Arial,sans-serif;color:var(--ink);position:relative}
.abs{position:absolute}
.serif{font-family:"Gilda Display",Georgia,serif;font-weight:400}
.accent{color:var(--green)}

/* header */
.brand{left:87px;top:38px;display:flex;align-items:center;gap:10px}
.brand-dot{width:30px;height:30px;border-radius:50%;background:var(--green)}
.brand-name{font-weight:700;font-size:17px;color:var(--navy);letter-spacing:.5px;text-transform:uppercase}
.nav{right:87px;top:40px;display:flex;align-items:center;gap:30px;font-size:11px;font-weight:500;color:var(--ink)}
.nav-cta{background:var(--green);color:var(--white);padding:9px 18px}

/* hero */
.hero-title{left:87px;top:128px;font-size:58px;line-height:62px;color:var(--ink)}
.est-label{left:603px;top:240px;font-size:9px;letter-spacing:2px;color:var(--muted);text-transform:uppercase}
.hero-photo{left:603px;top:257px;width:510px;height:689px;background:linear-gradient(160deg,#dcdad6 0%,#e9e8e5 55%,#f1f0ee 100%)}
.inquire{left:952px;top:202px;width:121px;height:110px;background:var(--green);color:var(--white);padding:14px 22px}
.inquire span{position:absolute;left:22px;bottom:16px;font-size:10px;font-weight:700;line-height:12px}

.panel{padding:56px 66px;color:var(--white)}
.panel h2{font-size:19px;font-weight:500;margin-bottom:26px}
.panel ul{list-style:none}
.panel li{display:flex;align-items:flex-start;gap:20px;font-size:10.5px;line-height:16px;margin-bottom:24px}
.panel li svg{flex:none;margin-top:-2px}
.panel-what{left:87px;top:471px;width:603px;height:275px;background:var(--navy)}
.panel-how{left:87px;top:946px;width:512px;height:276px;background:var(--green);padding:60px 60px}

.basket-photo{left:892px;top:1168px;width:308px;height:308px;background:radial-gradient(circle at 45% 40%,#f1e3e1 0%,#e3d8cc 40%,#cdb48e 70%,rgba(244,243,238,0) 72%)}

/* section headers */
.eyebrow{font-size:10px;letter-spacing:2px;color:var(--muted);text-transform:uppercase}
.section-title{font-size:58px;line-height:62px;color:var(--ink)}
.rule{width:93px;height:3px;background:var(--green)}

/* team */
.team-band{left:87px;top:1696px;width:1026px;height:162px;background:var(--band)}
.team{left:167px;top:1609px;display:flex;gap:12px}
.member{width:164px}
.member-photo{width:164px;height:159px;background:linear-gradient(160deg,#8a8478,#c9c1b4)}
.member:nth-child(2) .member-photo{background:linear-gradient(160deg,#5d5248,#c7b8a8)}
.member:nth-child(3) .member-photo{background:linear-gradient(160deg,#4f6b3e,#8e9a6a)}
.member:nth-child(4) .member-photo{background:linear-gradient(160deg,#c9ccd1,#e6e2dc)}
.member:nth-child(5) .member-photo{background:linear-gradient(160deg,#d9dde0,#ece7e4)}
.member-name{margin-top:14px;font-size:11px;font-weight:700;color:var(--ink)}
.member-role{font-size:9px;color:var(--muted);margin-top:2px}

/* products */
.products{left:87px;top:2196px;display:flex;gap:9px}
.product{position:relative;width:336px;height:275px}
.product-label{position:absolute;right:0;bottom:0;width:164px;height:91px;color:var(--white);font-size:11.5px;font-weight:700;line-height:14px;padding:26px 24px}
.p1{background:linear-gradient(150deg,#b2345b,#d6c03b 70%,#b2222c)}
.p2{background:linear-gradient(150deg,#6f7a58,#c6c3b6 55%,#8c7c5a)}
.p3{background:linear-gradient(150deg,#5b3d26,#a9794c 60%,#3a2a20)}

/* contact */
.contact{left:87px;top:2530px;width:1026px;height:499px;background:var(--white)}
.contact-info{position:absolute;left:116px;top:122px}
.contact-info .section-title{font-size:52px;line-height:56px;margin-top:14px}
.contact-info .rule{margin-top:14px}
.contact-person{margin-top:30px;font-size:11px;font-weight:700}
.contact-detail{font-size:10px;color:var(--muted);margin-top:6px}
.form{position:absolute;left:570px;top:117px;width:333px}
.field{border:1px solid var(--line);height:41px;margin-bottom:10px;font-size:10px;color:var(--muted);padding:15px 24px}
.field.msg{height:124px;margin-bottom:0}
.send{background:var(--green);color:var(--white);height:44px;font-size:11px;text-align:center;line-height:44px}
</style>
</head>
<body>

<header>
  <div class="abs brand"><div class="brand-dot"></div><span class="brand-name">Verdant Hollow</span></div>
  <nav class="abs nav"><span>What we do</span><span>About us</span><span>Products</span><span class="nav-cta">Talk to us</span></nav>
</header>

<section class="hero">
  <h1 class="abs hero-title serif">We are a<br><span class="accent">dedicated</span> team<br>assigned for<br>your account</h1>
  <p class="abs est-label">Established 1999</p>
  <div class="abs hero-photo" role="img" aria-label="White daffodils in a ribbed ceramic vase on a marble table"></div>
  <div class="abs inquire">
    <svg width="22" height="12" viewBox="0 0 22 12"><path d="M0 6h20M15 1l5 5-5 5" fill="none" stroke="#fff" stroke-width="1.4"/></svg>
    <span>Inquire<br>Now</span>
  </div>

  <div class="abs panel panel-what">
    <h2>What we do</h2>
    <ul>
      <li><svg width="20" height="20" viewBox="0 0 20 20"><path d="M3 17C3 8 9 3 18 3c0 9-6 14-15 14z" fill="#8cc63f"/></svg>Personalized Customer service</li>
      <li><svg width="20" height="20" viewBox="0 0 20 20"><path d="M3 17C3 8 9 3 18 3c0 9-6 14-15 14z" fill="#8cc63f"/></svg>Exclusively Mass market experience to meet high demands</li>
      <li><svg width="20" height="20" viewBox="0 0 20 20"><path d="M3 17C3 8 9 3 18 3c0 9-6 14-15 14z" fill="#8cc63f"/></svg>Dedicated team assigned to your account</li>
    </ul>
  </div>

  <div class="abs panel panel-how">
    <h2>How we do it</h2>
    <ul>
      <li><svg width="20" height="20" viewBox="0 0 20 20"><path d="M3 17C3 8 9 3 18 3c0 9-6 14-15 14z" fill="#d6eab8"/></svg>Partnerships with farms in COlombia, ecuador and costa rica</li>
      <li><svg width="20" height="20" viewBox="0 0 20 20"><path d="M3 17C3 8 9 3 18 3c0 9-6 14-15 14z" fill="#d6eab8"/></svg>Farm fresh delivered directly from cargo planes to state of the<br>art cooler facility at Delmont Airport</li>
      <li><svg width="20" height="20" viewBox="0 0 20 20"><path d="M3 17C3 8 9 3 18 3c0 9-6 14-15 14z" fill="#d6eab8"/></svg>Canopy trust?</li>
    </ul>
  </div>

  <div class="abs basket-photo" role="img" aria-label="Hand holding a wicker basket of pink and white roses"></div>
</section>

<section class="about">
  <p class="abs eyebrow" style="left:87px;top:1394px">About us</p>
  <h2 class="abs section-title serif" style="left:87px;top:1412px">Verdant Hollow Corp<br><span class="accent">Established 1999</span></h2>
  <div class="abs rule" style="left:87px;top:1551px"></div>

  <div class="abs team-band"></div>
  <div class="abs team">
    <div class="member"><div class="member-photo" role="img" aria-label="Portrait of Marla Pruett"></div><p class="member-name">Marla Pruett</p><p class="member-role">Founder</p></div>
    <div class="member"><div class="member-photo" role="img" aria-label="Portrait of Danielle Pruett"></div><p class="member-name">Danielle Pruett</p><p class="member-role">Account Executive</p></div>
    <div class="member"><div class="member-photo" role="img" aria-label="Portrait of Gerald Pruett"></div><p class="member-name">Gerald Pruett</p><p class="member-role">Director of Operations</p></div>
    <div class="member"><div class="member-photo" role="img" aria-label="Portrait of Rosalba Penwick"></div><p class="member-name">Rosalba Penwick</p><p class="member-role">Manager</p></div>
    <div class="member"><div class="member-photo" role="img" aria-label="Portrait of Natalia Ferreira"></div><p class="member-name">Natalia Ferreira</p><p class="member-role">Manager</p></div>
  </div>
</section>

<section class="product-section">
  <p class="abs eyebrow" style="left:87px;top:1980px">Products</p>
  <h2 class="abs section-title serif" style="left:87px;top:2000px">Products We<br><span class="accent">Sell</span></h2>
  <div class="abs rule" style="left:87px;top:2139px"></div>

  <div class="abs products">
    <div class="product p1" role="img" aria-label="Rows of colourful tulips"><div class="product-label" style="background:var(--navy)">Farm made<br>bouquets</div></div>
    <div class="product p2" role="img" aria-label="Table set with bunches of mixed flowers"><div class="product-label" style="background:var(--green)">Consumer<br>Bunches</div></div>
    <div class="product p3" role="img" aria-label="Shop counter with staff serving a customer"><div class="product-label" style="background:var(--orange)">Programs Tailored<br>to fit customer's<br>retail program</div></div>
  </div>
</section>

<section class="abs contact">
  <div class="contact-info">
    <p class="eyebrow">Contact information</p>
    <h2 class="section-title serif">Talk To <span class="accent">Us</span></h2>
    <div class="rule"></div>
    <p class="contact-person">Gerald and Danielle</p>
    <p class="contact-detail">+293 555 0142</p>
    <p class="contact-detail">gerald.danielle@verdanthollow.com</p>
  </div>
  <div class="form">
    <div class="field">Enter your email</div>
    <div class="field">Subject</div>
    <div class="field msg">Write your message here....</div>
    <div class="send">Send Message</div>
  </div>
</section>

</body>
</html>
```